beauty salon application for consumer

- Find your favorite beauty salons and spas or discover new places next to you with geolocation;
- Filter your search by price, distance, category and type of service;
- Never worry again about having to schedule during your work hours or about not having your calls answered when you want to book an appointment;
- Mark salons as favorites and be the first to be informed of exclusive discounts;
- Don’t ever forget your appointments with Glow Slot’s notifications;
- Compare prices, places and services freely, in a quick and practical way;
- Share reviews about services and places you go with other users and read their opinions;
- USER-FRIENDLY INTERFACE
- GALLERY
- OFFERS

similar interface with application name "pamperlane"

Industry/Entity Type

Beauty Salon

Font styles to use
Decorative
Script

Colors

Designer to choose colors to be used in the design.

Requirements
Must have
• Please have a look into these applications:
• 1- https://apps.example-store.test/gb/app/pamperlane/id572913804/?pid=korvasa&c=footer-link
• 2- https://apps.example-store.test/us/app/curlo-ltd-book-curl-style-glam-polish-services/id3948172065
• 3- https://market.sample-apps.test/store/apps/details?id=com.parlorvix.user&hl=en
• 4- https://apps.example-store.test/app/id463187209?mt=8
Nice to have
• Nice to give me a clear screenshots for main function of the application ,please see the above applications before giving me a design .

```html
<!DOCTYPE html>
<html lang="en">
<head>
<meta charset="utf-8">
<title>Beauty Salons – Log in</title>
<link rel="stylesheet" href="https://fonts.googleapis.com/css2?family=Dancing+Script:wght@500&family=Open+Sans:wght@400;700&display=swap">
<style>
  :root {
    --plum-deep: #52206b;
    --plum-mid: #7a2383;
    --magenta: #a51c86;
    --ring: #7b1f78;
    --white: #ffffff;
    --field-line: rgba(255, 255, 255, 0.85);
    --field-fill: rgba(255, 255, 255, 0.04);
    --button-text: #9a1c84;
  }
  * { margin: 0; padding: 0; box-sizing: border-box; }
  html, body { width: 675px; height: 1200px; overflow: hidden; }
  body { font-family: "Open Sans", Arial, sans-serif; color: var(--white); }

  .screen {
    position: relative;
    width: 675px;
    height: 1200px;
    overflow: hidden;
  }
  .backdrop {
    position: absolute;
    inset: 0;
    background:
      radial-gradient(ellipse 320px 420px at 120px 560px, rgba(170, 90, 150, 0.28), transparent 70%),
      linear-gradient(160deg, var(--plum-deep) 0%, var(--plum-mid) 45%, var(--magenta) 100%);
  }

  .status-bar {
    position: absolute;
    top: 0; left: 0; right: 0;
    height: 40px;
    display: flex;
    align-items: center;
    justify-content: space-between;
    padding: 0 14px 0 16px;
    font-family: "Helvetica Neue", Arial, sans-serif;
    font-size: 20px;
    letter-spacing: -0.2px;
  }
  .status-left, .status-right { display: flex; align-items: center; gap: 8px; }
  .signal { display: flex; gap: 3px; }
  .signal span { width: 10px; height: 10px; border-radius: 50%; background: var(--white); }
  .signal span.empty { background: transparent; border: 1.3px solid var(--white); }

  .brand-mark {
    position: absolute;
    left: 217px; top: 218px;
    width: 241px; height: 241px;
    border-radius: 50%;
    background: var(--white);
    border: 9px solid var(--ring);
  }
  .app-title {
    position: absolute;
    top: 465px; left: 0; right: 0;
    text-align: center;
    font-family: "Dancing Script", cursive;
    font-weight: 500;
    font-size: 64px;
    line-height: 1.2;
  }

  .login-form {
    position: absolute;
    left: 125px; top: 619px;
    width: 424px;
  }
  .field {
    display: flex;
    align-items: center;
    height: 68px;
    padding-left: 29px;
    border: 1px solid var(--field-line);
    border-radius: 34px;
    background: var(--field-fill);
    font-size: 16.5px;
  }
  .field + .field { margin-top: 34px; }
  .login-button {
    display: flex;
    align-items: center;
    justify-content: center;
    margin-top: 50px;
    height: 68px;
    border-radius: 34px;
    background: var(--white);
    color: var(--button-text);
    font-weight: 700;
    font-size: 17px;
    letter-spacing: 0.3px;
    box-shadow: 0 6px 12px rgba(60, 10, 60, 0.35);
  }
</style>
</head>
<body>
<main class="screen">
  <div class="backdrop" role="img" aria-label="Soft-focus beauty portrait photograph under a purple to magenta tint"></div>

  <header class="status-bar">
    <div class="status-left">
      <div class="signal"><span></span><span></span><span></span><span></span><span class="empty"></span></div>
      <span>Carrier</span>
      <svg width="20" height="16" viewBox="0 0 20 16" aria-hidden="true">
        <path d="M1 5.5a13 13 0 0 1 18 0" fill="none" stroke="#fff" stroke-width="2" stroke-linecap="round"/>
        <path d="M4.5 9a8 8 0 0 1 11 0" fill="none" stroke="#fff" stroke-width="2" stroke-linecap="round"/>
        <circle cx="10" cy="13" r="2" fill="#fff"/>
      </svg>
    </div>
    <div class="status-right">
      <svg width="20" height="20" viewBox="0 0 20 20" aria-hidden="true">
        <circle cx="10" cy="10" r="8.5" fill="none" stroke="#fff" stroke-width="1.5"/>
        <rect x="6.5" y="9" width="7" height="5" rx="1" fill="#fff"/>
        <path d="M8 9V7.5a2 2 0 0 1 4 0V9" fill="none" stroke="#fff" stroke-width="1.4"/>
      </svg>
      <span>100%</span>
      <svg width="42" height="18" viewBox="0 0 42 18" aria-hidden="true">
        <rect x="1" y="1" width="36" height="16" rx="3" fill="none" stroke="#fff" stroke-width="1.5"/>
        <rect x="3.5" y="3.5" width="31" height="11" rx="1.5" fill="#fff"/>
        <rect x="38.5" y="6" width="2.5" height="6" rx="1" fill="#fff"/>
      </svg>
    </div>
  </header>

  <div class="brand-mark" aria-hidden="true"></div>
  <h1 class="app-title">Beauty Salons</h1>

  <form class="login-form">
    <div class="field">Username</div>
    <div class="field">Password</div>
    <div class="login-button">LOG IN</div>
  </form>
</main>
</body>
</html>
```